Lumo Brew Premium Matcha brand Label

This is a label design project for a luxury tea brand. Feel free to be creative within the guidelines.
Attached to this project is a document called “Private Label Design Requirements” with the design guidelines and template. There is another document called "Lumo Brew Packaging Instructions" this has more details necessary to stick to the guidelines in the first document.

I have also attached the certifications to be included as well as different variations of the logo for you to use.

If you have any questions, I am here.
Updates

Target Market(s)

Young, active, fun, enjoy the finer things

```html
<!DOCTYPE html>
<html lang="en">
<head>
<meta charset="utf-8">
<title>Lumo Brew Ceremonial Matcha Label</title>
<link rel="stylesheet" href="https://fonts.googleapis.com/css2?family=Oswald:wght@500;600&family=Roboto+Condensed:wght@400&family=Kaushan+Script&display=swap">
<style>
  :root {
    --label-bg: #2b2725;
    --matcha: #8bb857;
    --white: #ffffff;
    --dieline: #d0101e;
    --canvas: #ffffff;
    --badge-blue: #3f6fb0;
    --badge-green: #2f8a4a;
  }
  html, body {
    margin: 0;
    padding: 0;
    width: 1200px;
    height: 1200px;
    overflow: hidden;
    background: var(--canvas);
  }
  .label {
    position: absolute;
    left: 34px;
    top: 488px;
    width: 1156px;
    height: 223px;
    background: var(--label-bg);
    color: var(--white);
    font-family: "Roboto Condensed", "Arial Narrow", sans-serif;
  }
  .dieline {
    position: absolute;
    left: 19px;
    top: 19px;
    width: 1112px;
    height: 187px;
    border: 2px solid var(--dieline);
    border-radius: 19px;
    box-sizing: border-box;
    z-index: 2;
  }
  .band {
    position: absolute;
    left: 0;
    top: 166px;
    width: 100%;
    height: 19px;
    background: var(--matcha);
    font-family: "Oswald", "Arial Narrow", sans-serif;
    font-weight: 600;
    font-size: 12.5px;
    letter-spacing: 3px;
    line-height: 19px;
  }
  .band span { position: absolute; top: 0; white-space: nowrap; }
  .band .origin { left: 73px; }
  .band .weight { left: 536px; }
  .band .storage { left: 845px; }

  .distributor { position: absolute; left: 73px; top: 100px; }
  .eyebrow {
    color: var(--matcha);
    font-size: 11.5px;
    text-transform: uppercase;
    margin: 0;
    line-height: 14px;
  }
  .distributor .company { font-size: 14px; margin: 2px 0 0; line-height: 18px; }
  .distributor .certifier { font-size: 12px; margin: 9px 0 0; line-height: 15px; }

  .brand { position: absolute; left: 476px; top: 40px; width: 240px; height: 120px; }
  .brand-mark {
    position: absolute; left: 20px; top: 6px;
    width: 44px; height: 44px; border-radius: 50%;
    background: var(--matcha);
  }
  .brand-name {
    position: absolute; left: 0; top: 56px;
    font-family: "Oswald", sans-serif; font-weight: 500;
    font-size: 15px; color: var(--white); white-space: nowrap;
  }
  .tagline {
    position: absolute; left: 94px; top: 13px;
    font-family: "Oswald", sans-serif; font-weight: 600;
    font-size: 19px; letter-spacing: 5px; line-height: 28px;
    margin: 0;
  }
  .tagline .organic { display: block; padding-left: 6px; }
  .brush-line {
    position: absolute; left: 93px; top: 71px;
    width: 116px; height: 2px; background: var(--white);
  }
  .product-name {
    position: absolute; left: -8px; top: 78px;
    font-family: "Kaushan Script", cursive;
    font-size: 31px; color: var(--matcha);
    white-space: nowrap; margin: 0;
  }

  .info { position: absolute; left: 841px; top: 38px; font-size: 12.5px; line-height: 15px; }
  .info .ingredients { margin: 2px 0 0; }
  .badges { position: absolute; left: 841px; top: 74px; }
  .badge-square { width: 44px; height: 32px; background: var(--badge-blue); border-radius: 2px; }
  .badge-circle {
    width: 40px; height: 40px; border-radius: 50%; margin-top: 10px;
    background: var(--badge-green); border: 2px solid var(--white);
  }
  .instructions { position: absolute; left: 898px; top: 76px; font-size: 12px; line-height: 14.6px; }
  .instructions ul { list-style: none; margin: 1px 0 0; padding: 0; }
  .instructions li::before { content: "• "; }
</style>
</head>
<body>
  <div class="label">
    <div class="dieline"></div>

    <div class="distributor">
      <p class="eyebrow">Distributed by</p>
      <p class="company">Lumo Brew Co. Riverton, Ga</p>
      <p class="certifier">Certified Organic by ORCA</p>
    </div>

    <div class="brand">
      <div class="brand-mark"></div>
      <div class="brand-name">Lumo Brew</div>
      <p class="tagline">PREMIUM<span class="organic">ORGANIC</span></p>
      <div class="brush-line"></div>
      <p class="product-name">Ceremonial Matcha</p>
    </div>

    <div class="info">
      <p class="eyebrow">Ingredients:</p>
      <p class="ingredients">Premium Organic Japanese Matcha Green Tea</p>
    </div>

    <div class="badges">
      <div class="badge-square" role="img" aria-label="Non-GMO certification badge"></div>
      <div class="badge-circle" role="img" aria-label="Organic certification badge"></div>
    </div>

    <div class="instructions">
      <p class="eyebrow">Instructions</p>
      <ul>
        <li>2 tsp of Matcha</li>
        <li>2oz of Water (170-180 degrees F)</li>
        <li>Whisk in a W formation until frothy</li>
        <li>Sweeten to taste</li>
      </ul>
    </div>

    <div class="band">
      <span class="origin">PRODUCT OF JAPAN</span>
      <span class="weight">NET WT: 30G</span>
      <span class="storage">KEEP REFRIGERATED FOR QUALITY</span>
    </div>
  </div>
</body>
</html>
```